Versicherungsmakler sucht Corporate Design (Logo, Visitenkarte, Briefpapier)
Zielgruppe
Optimale Beratung speziell auf die Zielgruppe werdende Eltern/Junge Familie abgestimmt.
Es geht darum, welche Absicherung (Versicherung, Vorsorge, Sparprodukte) gerade für diese spezielle Zielgruppe (und dort im Besonderen für die Kinder) essentiell ist. Leider werden diesen Kunden von Kollegen oft falsche beraten oder erhalten unbrauchbare oder zu teure Produkte. Mir ist es wichtig nur die richtigen und wichtigen Produkte zu vermitteln. Dies kann ich sehr gut beurteilen, weil ich selbst 2facher Familienvater bin (2 Jungs im Alter von1x 2 Jahren und1x 5 Monaten). Das ganze soll unabhängig von jeglichen Interessen der Versicherungswirtschaft und derer Unternehmen erfolgen, d.h. vollkommen auf die Anforderungen und Bedürfnisse des Kunden abgestimmt!!!
Aufgabenstellung
Ich suche nun noch einen zusätzlichen Markenauftritt für "NestWohl - klug geplant, sicher gebettet" (Logo, Visitenkarte, Briefpapier) für die o.g. spezielle Zielgruppe "Junge Familie/werdende Eltern". Der Fokus liegt auf der Vorsorge und Absicherung der Kinder.

```html
<!DOCTYPE html>
<html lang="de">
<head>
<meta charset="utf-8">
<title>NestWohl – Visitenkarte</title>
<link rel="stylesheet" href="https://fonts.googleapis.com/css2?family=Merriweather:ital,wght@0,300;0,400;1,300&family=Open+Sans:wght@300;400;700&display=swap">
<style>
  :root {
    --backdrop: #e9eaea;
    --card: #ffffff;
    --card-front: #f3f3f2;
    --brand-green: #0e8f6f;
    --band-start: #8cc449;
    --band-mid: #3fb386;
    --band-end: #14a3c7;
    --ink: #3a3a3a;
    --ink-soft: #505050;
    --shadow: rgba(0, 0, 0, 0.14);
  }
  * { margin: 0; padding: 0; box-sizing: border-box; }
  html, body {
    width: 1200px; height: 873px; overflow: hidden;
    background: var(--backdrop);
  }
  .sheet {
    width: 1200px; height: 873px;
    display: flex; align-items: center; justify-content: center; gap: 56px;
  }
  .card {
    position: relative;
    width: 520px; height: 336px;
    box-shadow: 0 6px 18px var(--shadow);
    overflow: hidden;
  }
  /* Front */
  .card--front {
    background: var(--card-front);
    display: flex; flex-direction: column; align-items: center; justify-content: center;
  }
  .brand {
    display: flex; align-items: center; gap: 14px;
  }
  .brand__dot {
    width: 26px; height: 26px; border-radius: 50%;
    background: var(--brand-green);
  }
  .brand__name {
    font-family: "Open Sans", sans-serif;
    font-weight: 700; font-size: 46px; letter-spacing: 0.5px;
    color: var(--brand-green);
  }
  .tagline {
    margin-top: 12px;
    font-family: "Merriweather", serif;
    font-weight: 300; font-size: 21px;
    color: var(--ink);
  }
  /* Back */
  .card--back { background: var(--card); }
  .band {
    position: absolute; left: 0; right: 0; bottom: 0; height: 30px;
    background: linear-gradient(90deg, var(--band-start), var(--band-mid) 55%, var(--band-end));
  }
  .person {
    position: absolute; right: 34px; top: 120px; text-align: right;
  }
  .person__name {
    font-family: "Open Sans", sans-serif;
    font-weight: 400; font-size: 25px; letter-spacing: 3px;
    color: var(--ink);
  }
  .person__role {
    margin-top: 4px;
    font-family: "Merriweather", serif;
    font-weight: 300; font-size: 13px;
    color: var(--ink-soft);
  }
  .contact {
    position: absolute; left: 30px; bottom: 52px;
    font-family: "Merriweather", serif;
    font-weight: 300; font-size: 11.5px; line-height: 1.55;
    color: var(--ink-soft);
    list-style: none;
  }
  .contact__gap { height: 10px; }
</style>
</head>
<body>
<main class="sheet">
  <section class="card card--front" aria-label="Vorderseite">
    <div class="brand">
      <span class="brand__dot"></span>
      <span class="brand__name">NestWohl</span>
    </div>
    <p class="tagline">Klug geplant, sicher gebettet.</p>
  </section>

  <section class="card card--back" aria-label="Rückseite">
    <div class="person">
      <p class="person__name">JONAS BRANDT</p>
      <p class="person__role">Geschäftsführung</p>
    </div>
    <ul class="contact">
      <li>Lindenweg 8</li>
      <li>34567 Birkenfeld</li>
      <li class="contact__gap"></li>
      <li>Tel.: +49 (0) 98 76 54 30</li>
      <li>Fax: +49 (0) 98 76 54 31</li>
      <li class="contact__gap"></li>
      <li>Email: info@nestwohl.de</li>
      <li>www.nestwohl.de</li>
    </ul>
    <div class="band"></div>
  </section>
</main>
</body>
</html>
```